Tranquil Meadow*

I am looking for it to be a flyer or a brochure. Something that sums up what my business is with little information. I do love the photo of the cat and dog I provided for the cover but I would also like to submit a photo for the back of the first ever pet hearse . My Pagemill page could be found under Tranquil Meadow Pet cremation and funeral services in Worcester Massachusetts. Maybe you can see exactly what I do. I am a pet service, one who offers assistance with the loss of your beloved pet. I am trying to stress to the public that they now have a choice and there is no need to leave their pets with their veterinarians to handle final arrangements. They now have someone like me. A one on one personal service to pick up your pet, at the place of death and walk it through the cremation or burial process. I will attach some things to give you some idea of what I need and what am I looking for thank you. Rosalind Debbet
PS.... I would love if you could possibly do some artwork on the photos of my purse. Remove the background I don't like the buildings and the sidewalk showing. Is that a possibility? Thanks. Also: I Also have a Pagemill under my business name if you would like to look at it.

Target Market(s)

Pet families, vets , young adults

Industry/Entity Type

Pet Care

Font styles to use
Decorative

Requirements
Must have
• Flyer that briefly describes pet cremation. It must specify that pet parents now have a choice when dealing with the loss of a pet. No longer necessary for deceased pet to stay with a veterinarian for cremation process. I Work one on one with families I offer merchandise such as urns, keepsakes, jewelry etc. I ensure fast and compassionate Service.
Nice to have
• I have included my logo and colors that I would like to use along with shades of gray or silver.
• I have included some ideas for photos I would like to keep the cat and dog photo on the cover and perhaps after adding some artwork to remove background using my purse on the back of the flyer it must have the name of the business and the only address would be Worcester, Massachusetts, no street. I have also enclosed that color scheme that I like along with purples grays in Silver’s. Thank you
Should not have
• Anything financial. Although I would like to specify that my prices are very comparable and customers will not be paying more for a private service.

```html
<!DOCTYPE html>
<html lang="en">
<head>
<meta charset="utf-8">
<title>Tranquil Meadow – Flyer</title>
<link href="https://fonts.googleapis.com/css2?family=Playball&family=Roboto:wght@300;400&family=Lora&display=swap" rel="stylesheet">
<style>
:root{
  --lilac:#8f9cd6;
  --lilac-soft:#a5b0e0;
  --lilac-text:#7f8bcb;
  --ink:#3c3c3c;
  --paper:#ffffff;
  --stage:#d9d9dc;
  --silver:#e4e5ea;
}
*{margin:0;padding:0;box-sizing:border-box}
html,body{width:1200px;height:762px;overflow:hidden;background:var(--stage)}
.canvas{position:relative;width:1200px;height:762px}
.page{position:absolute;top:45px;width:512px;height:672px;background:var(--paper);overflow:hidden;box-shadow:0 3px 10px rgba(0,0,0,.18);font-family:"Roboto",sans-serif;color:var(--ink)}
.page--front{left:60px}
.page--back{left:630px}
.abs{position:absolute}
.script{font-family:"Playball",cursive;font-weight:400}
.serif{font-family:"Lora",serif}

/* front */
.cover-photo{left:0;top:0;width:512px;height:262px;background:linear-gradient(180deg,#e8d6b9 0%,#d8bc97 35%,#b59c84 62%,#7d6a5f 100%)}
.band-svg{left:0;top:0}
.brand-mark{left:22px;top:268px;width:44px;height:44px;border-radius:50%;background:var(--paper)}
.brand-name{left:100px;top:252px;font-size:29px;color:var(--paper);white-space:nowrap}
.brand-sub{left:101px;top:293px;font-size:12.5px;color:var(--paper)}
.seal{left:362px;top:208px;width:124px;height:124px;border-radius:50%;background:var(--lilac-soft);border:3px solid rgba(255,255,255,.55);display:flex;align-items:center;justify-content:center;text-align:center;color:var(--paper);font-size:18px;line-height:22px}
.tagline{left:0;width:512px;top:362px;text-align:center;color:var(--lilac-text);font-size:17px;line-height:20px}
.front-body{left:17px;width:480px;top:411px;font-size:10px;line-height:13.5px;text-align:justify}
.contact-call{left:90px;width:320px;top:482px;text-align:center;font-size:10.5px}
.contact-name{left:90px;width:320px;top:497px;text-align:center;font-size:13px;color:var(--lilac-text)}
.social{display:flex;align-items:center;gap:5px;font-size:11px;color:var(--lilac-text)}
.social__dot{width:12px;height:12px;border-radius:50%;border:1.5px solid var(--lilac-text)}
.front-social{left:424px;top:488px}
.hearse-photo{left:18px;top:552px;width:256px;height:104px;border-radius:40px 60px 30px 30px;background:linear-gradient(180deg,#7d7f86 0%,#55575e 55%,#3a3b40 100%)}
.front-contacts{right:14px;top:581px;list-style:none;text-align:right;color:var(--paper);font-size:10.5px;line-height:19px}
.front-contacts li{display:flex;justify-content:flex-end;align-items:center;gap:8px}
.ico{width:13px;height:13px;flex:none}

/* back */
.back-mark{left:106px;top:40px;width:54px;height:54px;border-radius:50%;border:2px solid var(--lilac)}
.back-name{left:174px;top:46px;font-size:30px;color:#222;white-space:nowrap}
.back-sub{left:175px;top:84px;font-size:13.5px;color:#222}
.pill{left:39px;top:107px;width:443px;height:35px;border-radius:12px;background:var(--lilac);color:var(--paper);font-size:19px;display:flex;align-items:center;justify-content:center;box-shadow:0 8px 10px -6px rgba(120,130,190,.45)}
.intro{left:16px;width:480px;top:161px;text-align:center;font-weight:300;color:var(--lilac-text);font-size:13.5px;line-height:18.5px}
.back-body{left:16px;width:480px;font-size:9.3px;line-height:11.7px;text-align:justify}
.back-body--one{top:261px}
.back-body--two{top:307px}
.services{left:16px;top:381px;display:flex;gap:16px;list-style:none;font-size:11.5px}
.services li{display:flex;align-items:center;gap:5px}
.services li::before{content:"›";display:inline-flex;width:9px;height:9px;border-radius:50%;border:1px solid var(--lilac-text);color:var(--lilac-text);font-size:8px;line-height:7px;justify-content:center}
.back-social{left:420px;top:400px}
.round-photo{border-radius:50%;border:3px solid var(--paper);box-shadow:0 2px 6px rgba(0,0,0,.25)}
.round-photo--one{left:67px;top:437px;width:120px;height:120px;background:radial-gradient(circle at 50% 45%,#e9e7e4,#8b95a6)}
.round-photo--two{left:182px;top:426px;width:124px;height:124px;background:radial-gradient(circle at 50% 45%,#6b5340,#241c17)}
.round-photo--three{left:324px;top:431px;width:132px;height:132px;background:radial-gradient(circle at 50% 50%,#c79a66,#7c8fa6)}
.back-name-line{left:0;width:512px;top:584px;text-align:center;color:var(--paper);font-size:17px;line-height:24px}
.back-contacts{left:0;width:512px;top:637px;display:flex;justify-content:center;gap:16px;color:var(--paper);font-size:11px;list-style:none}
.back-contacts li{display:flex;align-items:center;gap:6px}
</style>
</head>
<body>
<main class="canvas">

  <section class="page page--front">
    <div class="abs cover-photo" role="img" aria-label="Photo of a woman and a white dog sitting together on a wooden jetty by a lake at sunset"></div>

    <svg class="abs band-svg" width="512" height="672" viewBox="0 0 512 672" aria-hidden="true">
      <path d="M0 240 Q220 205 512 262 L512 672 L0 672 Z" fill="var(--silver)"/>
      <path d="M0 250 Q220 215 512 270 L512 672 L0 672 Z" fill="var(--paper)"/>
      <path d="M0 255 Q220 220 512 275 L512 305 Q250 305 0 338 Z" fill="var(--lilac)"/>
      <path d="M0 585 Q250 520 512 545 L512 672 L0 672 Z" fill="var(--silver)"/>
      <path d="M0 598 Q250 535 512 556 L512 672 L0 672 Z" fill="var(--lilac)"/>
    </svg>

    <div class="abs brand-mark"></div>
    <h1 class="abs brand-name script">Tranquil Meadow</h1>
    <p class="abs brand-sub serif">Pet Cremation &amp; Funeral Services</p>

    <div class="abs seal script">Work<br>one on one<br>with families</div>

    <h2 class="abs tagline script">Pet Families.... Know you have a choice.<br>Personalized Service. Handled with Compassion and Dignity</h2>

    <p class="abs front-body">Pet parents now have a choice when dealing with the loss of a pet. No longer necessary for deceased pet to stay with a veterinarian for cremation process. A one on one personal service to pick up your pet, at the place of death and walk it through the cremation or burial process. I offer merchandise such as urns, keepsakes, jewelry etc. I ensure fast and compassionate Service. Affordable Prices!</p>

    <p class="abs contact-call">Contact me today for a free, no obligation consultation:</p>
    <p class="abs contact-name script">Rosalind Debbet</p>

    <div class="abs social front-social"><span class="social__dot"></span>Pagemill</div>

    <div class="abs hearse-photo" role="img" aria-label="Photo of the dark grey pet hearse with its background removed"></div>

    <ul class="abs front-contacts">
      <li>(555) 014-7320 <svg class="ico" viewBox="0 0 14 14"><circle cx="7" cy="7" r="7" fill="#fff"/><path d="M4.5 3.5l1.5 1.8-.8 1a5 5 0 0 0 2.5 2.5l1-.8 1.8 1.5-.8 1.2C7 10.5 3.6 7 3.3 4.3z" fill="var(--lilac)"/></svg></li>
      <li>info@tranquilmeadowpets.com <svg class="ico" viewBox="0 0 14 14"><circle cx="7" cy="7" r="7" fill="#fff"/><rect x="3.5" y="4.5" width="7" height="5" fill="none" stroke="var(--lilac)" stroke-width="1"/><path d="M3.5 4.5L7 7.5l3.5-3" fill="none" stroke="var(--lilac)" stroke-width="1"/></svg></li>
      <li>www.tranquilmeadowpets.com <svg class="ico" viewBox="0 0 14 14"><circle cx="7" cy="7" r="7" fill="#fff"/><circle cx="7" cy="7" r="3.8" fill="none" stroke="var(--lilac)" stroke-width="1"/><path d="M3.2 7h7.6M7 3.2v7.6" stroke="var(--lilac)" stroke-width="1"/></svg></li>
      <li>Alderbrook, ST 00000 <svg class="ico" viewBox="0 0 14 14"><circle cx="7" cy="7" r="7" fill="#fff"/><path d="M7 11S4.3 8 4.3 6a2.7 2.7 0 0 1 5.4 0C9.7 8 7 11 7 11z" fill="var(--lilac)"/><circle cx="7" cy="6" r="1" fill="#fff"/></svg></li>
    </ul>
  </section>

  <section class="page page--back">
    <div class="abs back-mark"></div>
    <h1 class="abs back-name script">Tranquil Meadow</h1>
    <p class="abs back-sub serif">Pet Cremation &amp; Funeral Services</p>

    <h2 class="abs pill script">Tranquil Meadow Pet Cremation &amp; Funeral Services</h2>

    <p class="abs intro">Pet parents now have a choice when dealing with the loss of a pet. No longer necessary for deceased pet to stay with a veterinarian for cremation process. A one on one personal service to pick up your pet, at the place of death and walk it through the cremation or burial process.</p>

    <p class="abs back-body back-body--one">Tranquil Meadow Pet Crematory &amp; Funeral Services is a family-owned pet crematory providing a dignified farewell to the beloved family pet. We operate on a foundation of ethics, compassion and respect for individual pet parents as well as the veterinary community as a whole.</p>

    <p class="abs back-body back-body--two">When death occurs in your pet family, there are many decisions to make. One of the most important is which funeral home and/or crematory to choose for your pet's final care. We understand the importance of this decision and strive to assist you every step of the way. When you lose your treasured companion, you lose a piece of your self and we understand that feeling. Providing you with the very best care and pet memorial service in Alderbrook County is our way of offering you our condolences, comfort, and peaceful wishes.</p>

    <ul class="abs services">
      <li>Cremation</li>
      <li>Memorial</li>
      <li>Burial</li>
    </ul>

    <div class="abs social back-social"><span class="social__dot"></span>Pagemill</div>

    <svg class="abs band-svg" width="512" height="672" viewBox="0 0 512 672" aria-hidden="true">
      <path d="M0 545 Q250 480 512 520 L512 672 L0 672 Z" fill="var(--silver)"/>
      <path d="M0 555 Q250 492 512 530 L512 672 L0 672 Z" fill="var(--lilac)"/>
    </svg>

    <div class="abs round-photo round-photo--one" role="img" aria-label="Round photo of a small white fluffy dog"></div>
    <div class="abs round-photo round-photo--two" role="img" aria-label="Round photo of a dark dog resting beside a tabby cat"></div>
    <div class="abs round-photo round-photo--three" role="img" aria-label="Round photo of a man holding his ginger cat close"></div>

    <p class="abs back-name-line script">Rosalind Debbet<br>Serving Alderbrook Country and surrounding areas</p>

    <ul class="abs back-contacts">
      <li><svg class="ico" viewBox="0 0 14 14"><circle cx="7" cy="7" r="7" fill="#fff"/><rect x="3.5" y="4.5" width="7" height="5" fill="none" stroke="var(--lilac)" stroke-width="1"/><path d="M3.5 4.5L7 7.5l3.5-3" fill="none" stroke="var(--lilac)" stroke-width="1"/></svg>info@tranquilmeadowpets.com</li>
      <li><svg class="ico" viewBox="0 0 14 14"><circle cx="7" cy="7" r="7" fill="#fff"/><path d="M4.5 3.5l1.5 1.8-.8 1a5 5 0 0 0 2.5 2.5l1-.8 1.8 1.5-.8 1.2C7 10.5 3.6 7 3.3 4.3z" fill="var(--lilac)"/></svg>(555) 014-7320</li>
      <li><svg class="ico" viewBox="0 0 14 14"><circle cx="7" cy="7" r="7" fill="#fff"/><circle cx="7" cy="7" r="3.8" fill="none" stroke="var(--lilac)" stroke-width="1"/><path d="M3.2 7h7.6M7 3.2v7.6" stroke="var(--lilac)" stroke-width="1"/></svg>www.tranquilmeadowpets.com</li>
    </ul>
  </section>

</main>
</body>
</html>
```